依頼詳細
■ デザイン

期間限定のキャンペーンメニュー(縦)です。

印刷掲示・印刷物配布・HPで使用します。

ファスティング(断食)をするためのリゾートホテルの宿泊客へむけたキャンペーンです。

テーマは、健康、デトックス、ダイエット、美しくなる

メインターゲットは、健康志向が高い女性、30歳~60歳

文字は大きく(50歳代が裸眼で見えるサイズ)

■使用する場所
ホテル内フロント・アロマルームで印刷物にラミネートをかけて掲示します
客室インフォメーションブックで印刷物を掲示します
HPに掲載します

■ 納品ファイル
JPG ai PDF

■添付ファイル
キャンペーン企画書
イメージ画像(必ずしも本画像が必須というわけではありません。お手持ちなどがありましたらご提案ください。)

■デザイン納期
4月上旬予定

■画像
お手持ちのものなど、無償使用できる画像でご提案ください。
場合により弊社所有の画像への入れ替えを提案することがあります。

■最下段には、2パターン店舗情報を記入してください。

■詳しくは企画書をご覧ください。ご不明点はメールでお問い合わせください

記載項目
サイズ
A4
ページ数
片面
希望イメージ
シンプル 複雑
単色 カラフル
暗い 明るい
日常 高級
遊び心 厳粛
未来的 伝統的
女性的 男性的
納品ファイル
• 高解像度JPG (.jpg)
• イラストレーター形式 (.ai)
■ 選んだ理由

本キャンペーンのイメージと、メニューの両方がとてもわかりやすく表現されていました。
1、2つのメニューの見やすい色と配置。
2、年齢層高い方にも文字サイズがほどよい。
3、本企画のテーマが表現されている。
4、季節感が感じられる。
5、シンプルななかにも柑橘が香り立つように盛り込まれている。
などが決め手となりました。

■ 提案者全員のお礼・コメント

この度は弊社コンペに多数ご応募くださいましてありがとうございました。とても素晴らしい作品が多く選出にはとても苦労をしました。また引き続きよろしくお願いいたします。

```html
<!DOCTYPE html>
<html lang="ja">
<head>
<meta charset="utf-8">
<title>爽健アロマデトックス</title>
<link rel="stylesheet" href="https://fonts.googleapis.com/css2?family=Noto+Sans+JP:wght@400;500;700;900&family=Noto+Serif+JP:wght@700;900&display=swap">
<style>
:root{
  --olive:#5a5420;
  --olive-dark:#3f3a14;
  --pink:#e2456e;
  --pink-soft:#f7c9d4;
  --green:#5aa53a;
  --green-soft:#cfe6b8;
  --red-price:#d9304f;
  --green-price:#3f9a2a;
  --cream:#f6f0dc;
  --ink:#3a3a2c;
  --white:#ffffff;
}
*{margin:0;padding:0;box-sizing:border-box}
html,body{width:849px;height:1200px;overflow:hidden;background:var(--white)}
body{font-family:"Noto Sans JP",sans-serif;color:var(--ink)}
.poster{position:relative;width:849px;height:1200px;background:var(--white);overflow:hidden}
.hero-photo{position:absolute;left:0;top:0;width:660px;height:322px;
  background:linear-gradient(120deg,#f3dccb 0%,#e9c5ab 40%,#d9b197 70%,#c9a385 100%)}
.title{position:absolute;left:672px;top:10px;z-index:2;writing-mode:vertical-rl;
  font-family:"Noto Serif JP",serif;font-weight:900;font-size:100px;line-height:1;
  letter-spacing:5px;color:var(--olive)}
.intro{position:absolute;left:30px;top:332px;width:630px;font-size:17px;font-weight:700;line-height:1.65;color:var(--ink)}
.menu{position:absolute;top:402px;width:300px}
.menu--left{left:26px}
.menu--right{left:344px}
.menu-head{display:flex;align-items:center;gap:8px;height:84px;border-radius:10px;padding:0 10px}
.menu--left .menu-head{background:var(--pink-soft)}
.menu--right .menu-head{background:var(--green-soft)}
.badge{width:66px;height:66px;border-radius:50%;display:flex;align-items:center;justify-content:center;
  font-family:"Noto Serif JP",serif;font-weight:900;font-size:28px;color:var(--white);line-height:1}
.menu--left .badge{background:var(--pink)}
.menu--right .badge{background:var(--green)}
.menu-name{font-weight:900;font-size:26px;line-height:1.15}
.menu--left .menu-name{color:var(--pink)}
.menu--right .menu-name{color:var(--green-price)}
.menu-lead{margin-top:8px;font-size:14px;font-weight:700;line-height:1.5}
.menu-note{margin-top:4px;font-size:11px;line-height:1.5;color:#6a6a5a;height:34px}
.price-list{list-style:none;margin-top:6px}
.price-list li{display:flex;align-items:center;height:52px;border-bottom:2px dotted #bbb}
.dur{width:62px;height:30px;border-radius:15px;display:flex;align-items:center;justify-content:center;
  font-size:16px;font-weight:700;color:var(--white);flex:none}
.menu--left .dur{background:var(--pink)}
.menu--right .dur{background:var(--green)}
.pick{font-size:11px;font-weight:900;color:#e07a1a;margin-left:4px;width:40px;line-height:1.2}
.yen{margin-left:auto;font-size:34px;font-weight:900;letter-spacing:-1px}
.menu--left .yen{color:var(--red-price)}
.menu--right .yen{color:var(--green-price)}
.campaign{position:absolute;left:26px;top:824px;width:618px}
.campaign-tag{position:absolute;left:250px;top:-16px;background:var(--green);color:var(--white);
  font-size:14px;font-weight:700;padding:2px 14px;border-radius:12px}
.campaign-box{border:3px solid var(--pink);border-radius:10px;height:58px;display:flex;align-items:center;padding:0 14px;gap:8px}
.campaign-label{font-size:25px;font-weight:900;color:var(--red-price)}
.campaign-text{font-size:21px;font-weight:700}
.campaign-text strong{color:var(--red-price);font-size:29px;font-weight:900}
.campaign-note{text-align:right;font-size:13px;margin-top:4px}
.info-band{position:absolute;left:0;top:932px;width:660px;height:56px;background:var(--olive);
  color:var(--white);font-size:26px;font-weight:700;text-align:center;line-height:56px}
.info{position:absolute;left:0;top:988px;width:849px;height:212px;background:var(--cream);padding:22px 30px;
  font-size:21px;font-weight:700;line-height:1.8;color:var(--olive-dark)}
</style>
</head>
<body>
<main class="poster">
  <div class="hero-photo" role="img" aria-label="アロマオイルで背中のトリートメントを受ける女性とプルメリアの花"></div>

  <h1 class="title">爽健アロマデトックス</h1>

  <p class="intro">伊豆特産ダイダイとグレープフルーツオイルで滞った毒素を分解して、リンパ活性トリートメントでデトックスをうながします。</p>

  <section class="menu menu--left">
    <div class="menu-head">
      <div class="badge">利尿</div>
      <div class="menu-name">デトックス<br>ボディ</div>
    </div>
    <p class="menu-lead">むくみや倦怠感を軽くするために、余分な水分の排出をサポートします</p>
    <p class="menu-note">グレープフルーツオイルに含まれるリモネン成分が、水分の巡りを整えます。</p>
    <ul class="price-list">
      <li><span class="dur">45分</span><span class="pick">おすすめ</span><span class="yen">¥6,300</span></li>
      <li><span class="dur">60分</span><span class="pick"></span><span class="yen">¥8,470</span></li>
      <li><span class="dur">90分</span><span class="pick"></span><span class="yen">¥12,540</span></li>
      <li><span class="dur">120分</span><span class="pick"></span><span class="yen">¥15,730</span></li>
    </ul>
  </section>

  <section class="menu menu--right">
    <div class="menu-head">
      <div class="badge">爽快</div>
      <div class="menu-name">デトックス<br>ボディ</div>
    </div>
    <p class="menu-lead">腸を活性化することで、老廃物の排出力を高めます</p>
    <p class="menu-note">伊豆ダイダイが腸の働きを助け、ペパーミントが温めながらデトックスを促します。</p>
    <ul class="price-list">
      <li><span class="dur">45分</span><span class="pick">おすすめ</span><span class="yen">¥6,300</span></li>
      <li><span class="dur">60分</span><span class="pick"></span><span class="yen">¥8,470</span></li>
      <li><span class="dur">90分</span><span class="pick"></span><span class="yen">¥12,540</span></li>
      <li><span class="dur">120分</span><span class="pick"></span><span class="yen">¥15,730</span></li>
    </ul>
  </section>

  <section class="campaign">
    <span class="campaign-tag">キャンペーン</span>
    <div class="campaign-box">
      <span class="campaign-label">事前割</span>
      <span class="campaign-text">▶前日までのご予約なら<strong>¥500</strong>割引します。</span>
    </div>
    <p class="campaign-note">※60分以上が対象です</p>
  </section>

  <div class="info-band">お問合せはフロントで承ります</div>
  <footer class="info">
    <p>営業時間▶15:00～22:00　／　受付時間▶15:00～18:00</p>
    <p>アロマサロン1階にございます &lt;全コース男女とも施術できます&gt;</p>
  </footer>
</main>
</body>
</html>
```